Swerve (nightclub flyer)

Nightclub flyer, guaranteed project. Text below (and please use logos, large):

SWERVE PRESENTS:

KORVEN (LOGO) B2B MARTY DELANO (LOGO)

+TOBBI RASK (smaller text)

10/26/17

2284 ELM LANE SACRAMENTO CA
21+ 10PM-2AM

HOUSE/TECHNO

A VELVET ORCHID ENTERTAINMENT (LOGO) PRODUCTION

Target Market(s)

House/Electronic Music Lovers

Industry/Entity Type

Night Club

Font styles to use
Sans Serif

Colors

Designer to choose colors to be used in the design.

Requirements
Must have
• Large logos for the dj names, or large block letter dj names (logos not necessary if it looks better without. But KORVEN b2b MARTY DELANO large and TOBBI RASK smaller on separate line
Nice to have
• Can include a classy female model but nothing cheesy or too sexy

```html
<!DOCTYPE html>
<html lang="en">
<head>
<meta charset="utf-8">
<title>Swerve Presents – Korven B2B Marty Delano</title>
<link rel="stylesheet" href="https://fonts.googleapis.com/css2?family=Montserrat:wght@300;500;700;900&family=Michroma&family=Oswald:wght@500&display=swap">
<style>
  :root {
    --olive-light: #a8ad7c;
    --olive: #6f7448;
    --olive-deep: #3d3f27;
    --night: #1c1a1c;
    --night-deep: #121113;
    --spark-red: #e8324a;
    --spark-pink: #ff8aa0;
    --ring-blue: #5fb7d4;
    --badge-black: #0b0b0d;
    --triangle: rgba(170, 178, 120, 0.72);
    --ink: #ffffff;
    --ink-soft: rgba(255, 255, 255, 0.88);
    --line: rgba(255, 255, 255, 0.55);
  }
  * { margin: 0; padding: 0; box-sizing: border-box; }
  html, body {
    width: 816px;
    height: 1200px;
    overflow: hidden;
    background: var(--night-deep);
  }
  .flyer {
    position: relative;
    width: 816px;
    height: 1200px;
    overflow: hidden;
    color: var(--ink);
    font-family: "Montserrat", Arial, sans-serif;
    text-align: center;
  }
  .backdrop {
    position: absolute;
    inset: 0;
    background:
      radial-gradient(ellipse 220px 90px at 70px 700px, rgba(255, 200, 215, 0.55), transparent 70%),
      radial-gradient(ellipse 220px 90px at 750px 720px, rgba(255, 200, 215, 0.5), transparent 70%),
      radial-gradient(ellipse 520px 130px at 408px 700px, rgba(232, 50, 74, 0.75), transparent 75%),
      linear-gradient(180deg, var(--olive-light) 0%, var(--olive) 22%, var(--olive-deep) 40%, #4a2a2c 55%, var(--night) 72%, var(--night-deep) 100%);
  }
  .decor {
    position: absolute;
    inset: 0;
  }
  .plus {
    position: absolute;
    left: 0;
    width: 100%;
    font-family: "Montserrat", Arial, sans-serif;
    font-weight: 300;
    font-size: 40px;
    line-height: 1;
  }
  .plus--top { top: 38px; }
  .plus--bottom { top: 1116px; }
  .presenter {
    position: absolute;
    top: 104px;
    width: 100%;
    font-size: 20px;
    font-weight: 500;
    letter-spacing: 0.5px;
  }
  .presenter strong { font-weight: 900; }
  .event-date {
    position: absolute;
    top: 132px;
    width: 100%;
    font-size: 46px;
    font-weight: 700;
    letter-spacing: 1px;
  }
  .dj-badge {
    position: absolute;
    left: 282px;
    top: 202px;
    width: 252px;
    height: 252px;
    border-radius: 50%;
    background: var(--badge-black);
    border: 4px solid var(--ring-blue);
    box-shadow: 0 0 0 5px var(--badge-black);
    display: flex;
    align-items: center;
    justify-content: center;
  }
  .dj-badge__name {
    font-family: "Michroma", Arial, sans-serif;
    font-size: 17px;
    color: var(--ink);
    letter-spacing: 1px;
    line-height: 1.5;
  }
  .headliner {
    position: absolute;
    top: 500px;
    width: 100%;
    font-family: "Michroma", Arial, sans-serif;
    font-size: 38px;
    letter-spacing: 1px;
  }
  .b2b {
    position: absolute;
    top: 570px;
    width: 100%;
    font-size: 42px;
    font-weight: 900;
  }
  .co-headliner {
    position: absolute;
    top: 632px;
    width: 100%;
    font-size: 88px;
    font-weight: 900;
    letter-spacing: 2px;
    line-height: 1.1;
  }
  .support {
    position: absolute;
    top: 788px;
    width: 100%;
    font-family: "Oswald", Arial, sans-serif;
    font-weight: 500;
    font-size: 23px;
    letter-spacing: 10px;
  }
  .production {
    position: absolute;
    top: 898px;
    width: 100%;
    font-size: 18px;
    font-weight: 700;
    letter-spacing: 1px;
  }
  .venue {
    position: absolute;
    top: 982px;
    width: 100%;
    font-size: 21px;
    font-weight: 700;
    line-height: 26px;
    letter-spacing: 0.5px;
  }
  .genre {
    position: absolute;
    top: 1042px;
    width: 100%;
    font-size: 29px;
    font-weight: 300;
    color: var(--ink-soft);
  }
</style>
</head>
<body>
<main class="flyer">
  <div class="backdrop" role="img" aria-label="Blurred city skyline at night with glowing red light sparks across the middle"></div>

  <svg class="decor" width="816" height="1200" viewBox="0 0 816 1200" aria-hidden="true">
    <polygon points="430,455 655,770 205,770" fill="none" stroke="var(--triangle)" stroke-width="34" stroke-linejoin="miter"/>
    <g stroke="var(--line)" stroke-width="1">
      <line x1="0" y1="270" x2="300" y2="510"/>
      <line x1="110" y1="305" x2="230" y2="410"/>
      <line x1="816" y1="270" x2="520" y2="510"/>
      <line x1="700" y1="300" x2="600" y2="400"/>
      <line x1="0" y1="1060" x2="270" y2="790"/>
      <line x1="30" y1="960" x2="200" y2="820"/>
      <line x1="816" y1="1070" x2="540" y2="790"/>
      <line x1="780" y1="960" x2="620" y2="830"/>
    </g>
  </svg>

  <div class="plus plus--top">+</div>
  <p class="presenter"><strong>SWERVE</strong> PRESENTS</p>
  <p class="event-date">10/26/2017</p>

  <div class="dj-badge">
    <span class="dj-badge__name">MARTY<br>DELANO</span>
  </div>

  <h1 class="headliner">MARTY DELANO</h1>
  <p class="b2b">B2B</p>
  <h2 class="co-headliner">KORVEN</h2>
  <p class="support">+TOBBI RASK</p>

  <p class="production">A VELVET ORCHID ENTERTAINMENT&nbsp; PRODUCTION</p>

  <p class="venue">2284 ELM LANE SACRAMENTO CA<br>21+ 10PM-2AM</p>
  <p class="genre">HOUSE + TECHNO</p>
  <div class="plus plus--bottom">+</div>
</main>
</body>
</html>
```